WORD Template for Training Manual called Quiet Harvest

I have written a training manual called Quiet Harvest. I need a design for the manual I can put the materials into for small groups of people to use.
This means a cover along with a page design that looks appealing but doesn't distract from the content.
We already have an organisational logo and colour scheme. It would be great to have at nine different page designs as the manual will have nine sessions of learning. So one design for each session of content.
I have uploaded some of the example materials we have designed from another designer as well so you can see the kind of look and feel our other materials have.
I have also uploaded the introduction and the first session of the content so you can use it to help shape the design.
As you will see in the sessions, each session has small group activities, discussion questions and a video content session for the group to watch. All nine sessions will be designed in a similar way.
There will also be a second booklet to design of daily reflections so a successful design for this workbook will lead to a second project with the same look and feel.
Updates
Need extra days to review
Target Market(s)
My target market is adults from 18-45
Industry/Entity Type
Christian Ministry
Look and feel

```html
<!DOCTYPE html>
<html lang="en">
<head>
<meta charset="utf-8">
<title>Quiet Harvest – Session Spread</title>
<link rel="stylesheet" href="https://fonts.googleapis.com/css2?family=Kalam:wght@400;700&family=Roboto:wght@400;500;700&display=swap">
<style>
  :root{
    --backdrop:#e3e3e3;
    --paper:#ffffff;
    --ink:#1f1f1f;
    --ink-soft:#2c2c2c;
    --brand-purple:#4d3f5e;
    --brand-green:#8cc63f;
    --heading-green:#5fae3c;
    --leaf-pale:#e7f0c6;
    --photo-warm:#c8763d;
    --photo-cool:#7fa7b5;
  }
  *{box-sizing:border-box;margin:0;padding:0}
  html,body{width:1200px;height:783px;overflow:hidden;background:var(--backdrop)}
  body{position:relative;font-family:"Roboto",Arial,sans-serif;color:var(--ink)}
  .page{position:absolute;background:var(--paper);overflow:hidden}
  .page--cover{left:25px;top:27px;width:557px;height:729px}
  .page--session{left:607px;top:25px;width:568px;height:733px}
  .abs{position:absolute}

  /* cover */
  .cover-photo{left:15px;top:20px;width:243px;height:347px;
    background:radial-gradient(ellipse at 45% 50%,#e9b17a 0%,var(--photo-warm) 40%,#7a3c20 80%);}
  .cover-photo-sky{left:15px;top:20px;width:243px;height:120px;
    background:linear-gradient(180deg,var(--photo-cool),rgba(127,167,181,0));}
  .leaf-shape{left:5px;top:439px;width:228px;height:300px;background:var(--leaf-pale);
    border-radius:90% 10% 0 0 / 100% 10% 0 0}
  .brand{left:286px;top:25px;display:flex;align-items:center;gap:7px}
  .brand-dot{width:16px;height:16px;border-radius:50%;background:var(--brand-green)}
  .brand-name{font-weight:700;font-size:17px;color:var(--brand-purple);letter-spacing:.2px}
  .cover-title{left:286px;top:66px;font-family:"Kalam",cursive;font-weight:700;font-size:25px;line-height:36px;color:var(--ink)}
  .cover-tagline{left:286px;top:108px;width:250px;font-weight:500;font-size:11.4px;line-height:17.6px;color:var(--ink-soft)}

  .intro-card{left:179px;top:159px;width:349px;height:543px;background:var(--paper);
    box-shadow:0 0 6px rgba(0,0,0,.18);padding:16px 22px 0 25px}
  .intro-heading{font-family:"Kalam",cursive;font-weight:700;font-size:21px;line-height:28px;margin-bottom:10px}
  .intro-body p{font-size:7.6px;line-height:12.65px;margin-bottom:12.6px;color:var(--ink-soft)}

  /* session */
  .session-title{left:36px;top:12px;font-family:"Kalam",cursive;font-weight:700;font-size:24px;line-height:34px}
  .col-left{left:36px;width:254px}
  .topic{top:51px;font-weight:700;font-size:10.2px;line-height:14.3px}
  .learn-head{top:108px;font-weight:700;font-size:10.2px;line-height:14px}
  .outcomes{top:128px;list-style:none;font-size:6.5px;line-height:10px}
  .outcomes li{display:flex;align-items:center;gap:7px;margin-bottom:10px}
  .body-text{font-size:9.1px;line-height:14.5px;color:var(--ink-soft)}
  .resources{top:175px;width:252px}
  .art{left:313px;top:0;width:255px;height:202px;
    background:radial-gradient(circle at 30% 35%,#f29ac0 0%,rgba(242,154,192,0) 35%),
      radial-gradient(circle at 70% 60%,#5a3f96 0%,rgba(90,63,150,0) 35%),
      radial-gradient(circle at 80% 20%,#f7d24a 0%,rgba(247,210,74,0) 30%),
      linear-gradient(135deg,#9bd24a,#4fc0d8);border-radius:0 0 0 40px}
  .video-head{left:36px;top:341px;font-family:"Kalam",cursive;font-weight:700;font-size:16px;line-height:24px;text-transform:uppercase;letter-spacing:.6px}
  .green-head{font-family:"Kalam",cursive;font-weight:700;color:var(--heading-green);font-size:14px;line-height:24px}
  .bullets{list-style:none}
  .bullets li{display:flex;gap:8px}
  .bullets svg{flex:none;margin-top:3px}
  .col-right{left:318px;top:218px;width:232px}
  .col-right .plain{margin-bottom:9px}
  .col-right .bullets{margin-bottom:8px}
  .col-right .bullets li{margin-bottom:6px}
  .page-number{right:12px;bottom:4px;font-family:"Times New Roman",serif;font-size:8.5px;color:#333}
</style>
</head>
<body>
<svg width="0" height="0" style="position:absolute" aria-hidden="true">
  <symbol id="arrow-bullet" viewBox="0 0 10 10">
    <circle cx="5" cy="5" r="4.2" fill="none" stroke="#8cc63f" stroke-width="1.3"/>
    <path d="M3 5h3.6M5.2 3.4L6.8 5 5.2 6.6" fill="none" stroke="#8cc63f" stroke-width="1.2" stroke-linecap="round"/>
  </symbol>
</svg>

<section class="page page--cover">
  <div class="abs cover-photo" role="img" aria-label="Photograph of a woman with closed eyes surrounded by flowing warm light"></div>
  <div class="abs cover-photo-sky" aria-hidden="true"></div>
  <div class="abs leaf-shape" role="img" aria-label="Large pale green leaf decoration"></div>
  <div class="abs brand"><span class="brand-dot"></span><span class="brand-name">Fenwick Ministries</span></div>
  <h1 class="abs cover-title">Quiet Harvest</h1>
  <p class="abs cover-tagline">60 Days of learning that will teach you to leap from safety into the adventure of your life!</p>

  <article class="abs intro-card">
    <h2 class="intro-heading">Introduction</h2>
    <div class="intro-body">
      <p>When I was a young boy, I loved games and adventures. Games I played with Mum and Dad, and the adventures I read in books or created in my imagination and played out in the backyard. One of my favourite games was pretty simple. I would start at the end of the hallway in our house, Mum would call me, and I would run down the hallway as fast as I could. When I got to the end of the hallway, I would leap into the air through the doorway into the kitchen, and she would catch me and give me a great big hug.</p>
      <p>One day I put my fertile imagination and this game together and decided to play the game with Dad. Dad came home from work one afternoon through the front door and headed down the hallway to the kitchen. He stood in the kitchen in clear view and was chatting with Mum. I imagined what it would be like to play this game with Dad; in my head, it all played out beautifully.</p>
      <p>So, I yelled out, “Dad, Dad, “and took off down the hallway as fast as my legs could carry me. Dad had a look in my direction and then looked back to Mum. I kept running down the hallway, and Dad looked back at me and waited for me to arrive; I got to the Kitchen doorway and leapt as high and as far as I had ever jumped in my life…</p>
      <p>I regained consciousness with blood running down my face and my dad saying, “I didn’t know the game”. Mum was trying to stop the bleeding, and my brain was struggling to figure out what had happened. It seems I had flown across the kitchen headfirst into the cupboards, cutting my head open on the cupboard door handle, a scar I retain to this day.</p>
      <p>For me, following Jesus can be a little like this, I think I have it figured out, and I embark on what I think God wants me to do; I hit my head and then wonder what on earth happened. At that point, wounded and bruised, God always brings me back to the basics. He calls me back to his simple commands to love others the way he loves me, to announce that He is here, that He loves others too, and to gather with other followers for worship, encouragement and support so we can follow Jesus together.</p>
      <p>Quiet Harvest takes followers of Jesus through those basic commands and their implications for our everyday life. My goal in developing this material is to teach you how to look at the world around you through Jesus’ eyes, to see people the way He sees them, and then to pursue His mission as a part of your everyday being and doing. To move beyond believing in God and accepting his Grace and Forgiveness to living his commands faithfully and, by doing so, being part of God’s transformation project, just like He always intended.</p>
    </div>
  </article>
</section>

<section class="page page--session">
  <h2 class="abs session-title">What is Love?</h2>
  <p class="abs col-left topic">Topic: Love is a choice, followed by an action to step into the world of another and act self-sacrificially in that person’s best interests.</p>
  <h3 class="abs col-left learn-head">In this session, participants will learn</h3>
  <ul class="abs col-left outcomes" style="width:270px">
    <li><svg width="6" height="6"><use href="#arrow-bullet"/></svg>Explain the biblical concept of Love as expressed by God through Jesus Christ</li>
    <li><svg width="6" height="6"><use href="#arrow-bullet"/></svg>Describe how they can express love towards others in their context.</li>
  </ul>
  <div class="abs col-left body-text resources">
    <p>Resources you will need:</p>
    <p>A3 Paper for drawing and Coloured Pencils/Textas for drawing.</p>
    <p>Pre-video activity</p>
    <p>In groups of 3, draw a picture representing the moment the father welcomes his prodigal son home (Luke 15:11-32). Think about what it was the father was saying through his actions. What was the son saying through his actions? What was being expressed between them? This is not a picture of the moment like a photograph, but rather a picture representing it in a way that might not even have the father and son in it.</p>
  </div>
  <div class="abs art" role="img" aria-label="Colourful illustration of hands, hearts and leaves in green, pink, purple and blue"></div>

  <h3 class="abs video-head">Show video content<br>for What is Love?</h3>
  <h4 class="abs col-left green-head" style="top:397px">Large Group Discussion</h4>
  <ul class="abs col-left bullets body-text" style="top:430px">
    <li style="margin-bottom:13px"><svg width="10" height="10"><use href="#arrow-bullet"/></svg><span>Was there any content in the video that was new to you or expressed in a way that you hadn’t heard before?</span></li>
    <li><svg width="10" height="10"><use href="#arrow-bullet"/></svg><span>What were the key points being made in the video?<br>Small Group Discussion</span></li>
  </ul>
  <h4 class="abs col-left green-head" style="top:510px">In groups of three, discuss the<br>following questions</h4>
  <ul class="abs col-left bullets body-text" style="top:570px">
    <li style="margin-bottom:13px"><svg width="10" height="10"><use href="#arrow-bullet"/></svg><span>When Jesus was born, God entered our world. God incarnate, God in human flesh. This is the moment God's revolution began when God chose to come and dwell amongst us. This is the heart of God's mission, to go and live with His created humans.</span></li>
    <li><svg width="10" height="10"><use href="#arrow-bullet"/></svg><span>What does it mean to you that God wants to live in your world and understand what life is like for you?</span></li>
  </ul>

  <div class="abs col-right body-text">
    <p class="plain">In doing this, God has expressed His love for each and every person He has created. Paul expressed this best in Romans 5:6-8, writing, "You see, just at the right time, when we were still powerless, Christ died for the ungodly. Very rarely will anyone die for a righteous person, though for a good person, someone might possibly dare to die. But God demonstrates his own love for us in this: While we were still sinners, Christ died for us.”</p>
    <ul class="bullets">
      <li><svg width="10" height="10"><use href="#arrow-bullet"/></svg><span>What does it mean to you that God’s love for you is something you haven’t and can’t earn?</span></li>
      <li><svg width="10" height="10"><use href="#arrow-bullet"/></svg><span>What example does that set for each of us in how we love others?</span></li>
    </ul>
    <p class="plain">To love someone means choosing to enter into their world in the same way that God entered into our world. Once we have chosen to do this, we pick up our cross and prepare to sacrifice our self-interests to benefit the other person whom Jesus loves.</p>
    <ul class="bullets">
      <li><svg width="10" height="10"><use href="#arrow-bullet"/></svg><span>What are some of the potential costs of living this way?</span></li>
    </ul>
    <p class="plain">Read Romans 5:1-5</p>
    <ul class="bullets">
      <li><svg width="10" height="10"><use href="#arrow-bullet"/></svg><span>Does anyone have an example to share of their decision to love someone causing personal suffering? Can you relate to what Paul has written about suffering leading to resilience, character, and hope?</span></li>
      <li><svg width="10" height="10"><use href="#arrow-bullet"/></svg><span>Large Group Discussion<br>Share with the larger group what your group has learned together as you have worked through the questions.<br>Close the evening with a time of prayer.</span></li>
    </ul>
  </div>
</section>

<span class="abs page-number">C 25</span>
</body>
</html>
```